tazelbox

I would like a label that would print outside of 24oz cups in Orange. The main ingredient for the cups will be noodles. Just like my lumbix projects, I would accept any funky, creative, funny and well noticed labels. Please keep in mind that we are a Korean food joint.

```html
<!DOCTYPE html>
<html lang="en">
<head>
<meta charset="utf-8">
<title>Tazelbox Noodle Cup Label</title>
<link rel="stylesheet" href="https://fonts.googleapis.com/css2?family=Arimo:wght@400;700&family=Bowlby+One&display=swap">
<style>
  :root {
    --paper: #ffffff;
    --frame: #8a8a8a;
    --brand-red: #e3242b;
    --band-yellow: #fff200;
    --ink: #231f20;
    --panel: rgba(255, 255, 255, 0.72);
    --noodle-gold: #d9a25a;
    --noodle-orange: #c9622e;
    --bowl-brown: #7a5236;
    --table-cream: #efe3d2;
    --pepper-red: #e2462a;
  }
  * { box-sizing: border-box; margin: 0; padding: 0; }
  html, body { width: 1200px; height: 521px; overflow: hidden; background: var(--paper); }
  .canvas {
    position: relative; width: 1200px; height: 521px;
    border: 1px solid var(--frame); background: var(--paper);
    font-family: "Arimo", Arial, sans-serif; color: var(--ink);
  }
  .label {
    position: absolute; inset: 0;
    clip-path: polygon(29px 42px, 1172px 42px, 1063px 504px, 134px 504px);
    background: var(--table-cream);
  }
  .photo { position: absolute; top: 42px; height: 462px; }
  .photo--left {
    left: 0; width: 510px;
    background:
      radial-gradient(ellipse 48% 46% at 46% 52%, var(--noodle-gold) 0%, var(--noodle-orange) 55%, var(--bowl-brown) 78%, rgba(122,82,54,0) 86%),
      linear-gradient(160deg, var(--pepper-red) 0%, var(--table-cream) 30%, var(--table-cream) 100%);
  }
  .photo--right {
    left: 690px; width: 510px;
    background:
      radial-gradient(ellipse 48% 46% at 40% 52%, var(--noodle-gold) 0%, var(--noodle-orange) 55%, var(--bowl-brown) 78%, rgba(122,82,54,0) 86%),
      linear-gradient(200deg, var(--pepper-red) 0%, var(--table-cream) 30%, var(--table-cream) 100%);
  }
  .band {
    position: absolute; left: 508px; top: 42px; width: 182px; height: 462px;
    background: var(--band-yellow);
  }
  .brand-badge {
    position: absolute; left: 454px; top: 102px; width: 264px; height: 264px;
    border-radius: 50%; background: var(--brand-red);
  }
  .brand-badge::after {
    content: ""; position: absolute; inset: 12px;
    border: 2px solid var(--band-yellow); border-radius: 50%;
  }
  .brand-name {
    position: absolute; left: 0; right: 0; top: 104px;
    text-align: center; color: #fff; font-size: 42px; font-weight: 400;
  }
  .product-title {
    position: absolute; left: 420px; width: 360px; top: 352px;
    text-align: center; font-family: "Bowlby One", Impact, sans-serif;
    font-size: 58px; letter-spacing: 3px; line-height: 1; font-weight: 400;
  }
  .flavour {
    position: absolute; left: 410px; width: 380px; top: 430px;
    text-align: center; font-weight: 700; font-size: 23px;
  }
  .nutrition {
    position: absolute; left: 138px; top: 90px; width: 210px; height: 276px;
    background: var(--panel); padding: 10px 6px 0 8px;
  }
  .nutrition__title {
    font-weight: 700; font-size: 22px; padding-bottom: 2px;
    border-bottom: 4px solid var(--ink);
  }
  .nutrition__table { width: 100%; border-collapse: collapse; font-size: 14px; }
  .nutrition__table td { border-bottom: 1px solid var(--ink); vertical-align: bottom; padding: 2px 0; }
  .nutrition__table td:first-child { width: 128px; border-right: 1px solid var(--ink); text-decoration: underline; }
  .nutrition__table td:last-child { padding-left: 4px; }
  .nutrition__table tr.total td { border-bottom: 3px solid var(--ink); font-size: 16px; }
  .cooking-note {
    position: absolute; left: 142px; top: 378px; width: 206px;
    font-size: 8.5px; line-height: 1.25;
  }
</style>
</head>
<body>
  <div class="canvas">
    <div class="label">
      <div class="photo photo--left" role="img" aria-label="Photo of a bowl of masala noodles with chopsticks, peppers and carrots"></div>
      <div class="photo photo--right" role="img" aria-label="Photo of a bowl of spicy masala noodles with chopsticks and vegetables"></div>
      <div class="band"></div>

      <div class="nutrition">
        <h2 class="nutrition__title">Nutrition Facts</h2>
        <table class="nutrition__table">
          <tr style="height:34px"><td>Protien</td><td></td></tr>
          <tr style="height:34px"><td>Sugar</td><td>1.35ml</td></tr>
          <tr style="height:26px"><td>Potacium</td><td>1.35ml</td></tr>
          <tr style="height:22px"><td>Magnisium</td><td>1.35ml</td></tr>
          <tr style="height:38px"><td>Raw Salt</td><td>1.35ml</td></tr>
          <tr class="total" style="height:40px"><td>Total in ml</td><td>1.35ml</td></tr>
        </table>
      </div>
      <p class="cooking-note">Hand-pulled wheat noodles tossed in a bold masala sauce with chilli, garlic and spring onion. Add hot water, close the lid and wait three minutes. Stir well before eating. Best enjoyed hot with kimchi on the side. Store in a cool dry place away from sunlight.</p>

      <div class="brand-badge"><span class="brand-name">Tazelbox</span></div>
      <h1 class="product-title">NOODLES</h1>
      <p class="flavour">Delicious Masala Flavour</p>
    </div>
  </div>
</body>
</html>
```